Homvuk Business Card Project showing the logo and a bellan image on the rear

Design a whacky but professional business card, the logo is for the front and the Bellan image is for the rear. Happy to consider other open source Bellan Images if the designer wants to select one from the web. Homvuk is a competitor to TKU.com.au and Parcelo.com.au and is based around every property in Australia

Target Market(s)

Business

Contact Information for Business Card

Name, Title, Email, Web, Phone Number

Font styles to use
Other font styles liked:
• avenir

Requirements
Must have
• Image on Back logo on front
Nice to have
• Happy to consider other images on rear, preftably Oskar Bellan. Image supplied I own, we can use open source other Bellan Images

```html
<!DOCTYPE html>
<html lang="en">
<head>
<meta charset="utf-8">
<title>Homvuk Business Card</title>
<link href="https://fonts.googleapis.com/css2?family=Nunito+Sans:wght@400;600;800&display=swap" rel="stylesheet">
<style>
  :root {
    --bg: #1c1c1c;
    --orange: #f39021;
    --ink: #111111;
    --card-dark: #1f1f1f;
    --white: #ffffff;
    --sky: #3f78c9;
    --sky-light: #5fb0e6;
  }
  * { box-sizing: border-box; margin: 0; padding: 0; }
  html, body { width: 1200px; height: 988px; overflow: hidden; }
  body {
    background: var(--bg);
    font-family: "Nunito Sans", sans-serif;
    position: relative;
  }
  .card {
    position: absolute;
    width: 640px;
    height: 366px;
    border-radius: 22px;
    overflow: hidden;
  }
  /* rear side */
  .card--rear { left: 60px; top: 70px; }
  .rear-artwork {
    position: absolute; inset: 0;
    background: linear-gradient(170deg, var(--sky-light) 0%, var(--sky) 30%, #d8742a 60%, #2f7a3a 78%, #c9453a 100%);
  }
  .brand {
    position: absolute;
    display: flex;
    align-items: center;
    gap: 14px;
    font-weight: 800;
    letter-spacing: 1px;
  }
  .brand__mark {
    width: 46px; height: 46px;
    background: var(--orange);
  }
  .card--rear .brand {
    left: 50%; top: 50%;
    transform: translate(-50%, -50%);
    color: var(--white);
    font-size: 76px;
  }
  .card--rear .brand__mark { width: 62px; height: 62px; }

  /* front side */
  .card--front { left: 500px; top: 560px; background: var(--white); }
  .front-wave { position: absolute; inset: 0; }
  .card--front .brand {
    left: 46px; top: 140px;
    color: var(--ink);
    font-size: 60px;
  }
  .person {
    position: absolute;
    right: 48px; top: 30px;
    text-align: right;
  }
  .person__name {
    color: var(--orange);
    font-weight: 800;
    font-size: 26px;
    letter-spacing: 1px;
    text-transform: uppercase;
  }
  .person__title {
    color: var(--ink);
    font-size: 16px;
    letter-spacing: 1px;
    margin-top: -2px;
  }
  .contact {
    position: absolute;
    right: 26px; top: 168px;
    list-style: none;
    text-align: right;
    color: var(--white);
    font-size: 15px;
    line-height: 23px;
    letter-spacing: 0.5px;
  }
  .contact li { display: flex; justify-content: flex-end; align-items: center; gap: 8px; }
  .contact__icon {
    width: 16px; height: 16px;
    border-radius: 50%;
    background: var(--orange);
    display: inline-flex; align-items: center; justify-content: center;
  }
  .contact__spacer { width: 16px; }
</style>
</head>
<body>

<section class="card card--rear">
  <div class="rear-artwork" role="img" aria-label="Colourful pop-art cityscape of cartoon buildings under a blue sky with sun, clouds and stars"></div>
  <div class="brand"><span class="brand__mark"></span>Homvuk</div>
</section>

<section class="card card--front">
  <svg class="front-wave" viewBox="0 0 640 366" preserveAspectRatio="none">
    <path d="M0,366 L0,336 C200,340 300,300 380,215 C450,140 520,116 640,108 L640,366 Z" fill="var(--card-dark)"/>
    <path d="M150,330 C270,320 320,282 372,210 C440,126 520,104 600,98" fill="none" stroke="var(--orange)" stroke-width="4"/>
  </svg>

  <div class="brand"><span class="brand__mark"></span>Homvuk</div>

  <div class="person">
    <p class="person__name">Tomas Wrenley</p>
    <p class="person__title">Executive Producer</p>
  </div>

  <ul class="contact">
    <li>418 Kestrel Road<span class="contact__spacer"></span></li>
    <li>Harlow Vale QLD 4870<span class="contact__spacer"></span></li>
    <li>555-210-4417
      <span class="contact__icon"><svg width="10" height="10" viewBox="0 0 10 10"><path d="M2 1 L4 1 L4.6 3 L3.4 3.8 C4 5.2 4.8 6 6.2 6.6 L7 5.4 L9 6 L9 8 C5 9 1 5 2 1 Z" fill="#fff"/></svg></span>
    </li>
    <li>Tomas@homvuk.com.au
      <span class="contact__icon"><svg width="10" height="10" viewBox="0 0 10 10"><rect x="1" y="2.5" width="8" height="5.5" fill="#fff"/><path d="M1 2.5 L5 5.5 L9 2.5" fill="none" stroke="var(--orange)" stroke-width="1"/></svg></span>
    </li>
    <li>www.homvuk.com.au
      <span class="contact__icon"><svg width="10" height="10" viewBox="0 0 10 10"><circle cx="5" cy="5" r="3.6" fill="none" stroke="#fff" stroke-width="1.2"/><path d="M1.4 5 H8.6 M5 1.4 V8.6" stroke="#fff" stroke-width="1"/></svg></span>
    </li>
  </ul>
</section>

</body>
</html>
```